Granite Surface Works, Inc. Business Card

New business, we do epoxy, polishing concrete, underlayment, fluid applied flooring, sound proofing, double sided, will need 3 sets of cards with 3 different names and phone numbers.
Company: Granite Surface Works, Inc.
Address and Phone: 6339 Charlotte Pike PMB 2183Nashville, TN 37209
(615) 384-7190
www.granitesurfaceworks.example

Target Market(s)

General Contractors, Contractors, Architects

Contact Information for Business Card

1st Card: Derek Halvorsen C. 708.214.8573 e. derek@granitesurfaceworks.example
Vice President
2nd Card: Morgan Brasfield C. 708.361.5847 e. morgan@granitesurfaceworks.example
President
3rd Card: Raj Oti C. 405.617.3328 e. raj@granitesurfaceworks.example
Managing Partner

Font styles to use
Serif
Sans Serif

Requirements
Must have
• Professional Clean Design, Implement colors from Logo or nicely contrasting
Nice to have
• N/A

```html
<!DOCTYPE html>
<html lang="en">
<head>
<meta charset="utf-8">
<title>Granite Surface Works, Inc. — Business Card</title>
<link rel="stylesheet" href="https://fonts.googleapis.com/css2?family=Poppins:wght@400;500;700&display=swap">
<style>
  :root {
    --brand-blue: #1a6cc2;
    --brand-green: #6b9d3c;
    --ink: #1f1f1f;
    --navy: #0e2f5c;
    --paper: #ffffff;
    --stage: #e9e6e1;
  }
  * { box-sizing: border-box; margin: 0; padding: 0; }
  html, body { width: 1200px; height: 900px; overflow: hidden; }
  body {
    background: var(--stage);
    font-family: "Poppins", sans-serif;
    position: relative;
  }
  .card {
    position: absolute;
    border-radius: 22px;
    overflow: hidden;
    box-shadow: 0 10px 28px rgba(0,0,0,0.18);
  }

  /* Front: vertical white card */
  .card-front {
    left: 80px; top: 130px;
    width: 370px; height: 640px;
    background: var(--paper);
  }
  .front-brand {
    position: absolute; left: 38px; right: 38px; top: 60px;
    display: flex; align-items: center; gap: 14px;
  }
  .brand-square {
    width: 46px; height: 46px; flex: none;
    background: var(--brand-green);
  }
  .brand-name {
    font-weight: 700; color: var(--ink);
    font-size: 25px; line-height: 1.12;
  }
  .contact-block {
    position: absolute; left: 38px; right: 30px; top: 200px;
  }
  .person-name {
    font-weight: 700; color: var(--brand-blue);
    font-size: 27px; line-height: 1.1;
  }
  .person-title {
    font-weight: 400; color: var(--brand-green);
    font-size: 17px; margin-top: 2px;
  }
  .contact-icons { display: flex; gap: 8px; margin: 20px 0 14px; }
  .contact-icons svg { width: 26px; height: 26px; }
  .contact-line {
    font-size: 15.5px; color: var(--ink); line-height: 1.65;
    white-space: nowrap;
  }
  .contact-line .accent { color: var(--brand-blue); }
  .address-band {
    position: absolute; left: 0; right: 0; bottom: 0; height: 160px;
    background: var(--brand-blue);
    padding: 40px 38px 0;
  }
  .address-band svg { width: 22px; height: 28px; display: block; margin-bottom: 10px; }
  .address-line {
    color: var(--navy); font-size: 17px; font-weight: 500; line-height: 1.4;
  }

  /* Back: horizontal blue card */
  .card-back {
    left: 500px; top: 250px;
    width: 630px; height: 370px;
    background: var(--brand-blue);
  }
  .back-brand {
    position: absolute; left: 0; right: 0; top: 115px;
    display: flex; align-items: center; justify-content: center; gap: 18px;
  }
  .back-brand .brand-square { width: 58px; height: 58px; }
  .back-brand .brand-name { font-size: 34px; color: var(--ink); }
  .back-web {
    position: absolute; left: 0; right: 0; top: 215px;
    text-align: center; color: var(--ink); font-size: 20px;
  }
</style>
</head>
<body>

<section class="card card-front" aria-label="Business card front">
  <div class="front-brand">
    <span class="brand-square"></span>
    <span class="brand-name">Granite Surface Works</span>
  </div>

  <div class="contact-block">
    <p class="person-name">Derek Halvorsen</p>
    <p class="person-title">Vice President</p>
    <div class="contact-icons">
      <svg viewBox="0 0 26 26" aria-label="Phone"><circle cx="13" cy="13" r="12" fill="var(--brand-blue)"/><path d="M9 7.5c.6-.5 1.4-.4 1.8.2l1 1.6c.3.5.2 1.1-.2 1.5l-.8.7c.6 1.4 1.6 2.5 3 3.1l.7-.8c.4-.4 1-.5 1.5-.2l1.6 1c.6.4.7 1.2.2 1.8l-.9 1c-.6.6-1.5.8-2.3.5-3.2-1.2-5.6-3.6-6.8-6.8-.3-.8-.1-1.7.5-2.3z" fill="#fff"/></svg>
      <svg viewBox="0 0 26 26" aria-label="Email"><circle cx="13" cy="13" r="12" fill="var(--brand-blue)"/><rect x="7" y="8.5" width="12" height="9" rx="1" fill="#fff"/><path d="M7.5 9.2 13 13.5l5.5-4.3" fill="none" stroke="var(--brand-blue)" stroke-width="1.3"/></svg>
      <svg viewBox="0 0 26 26" aria-label="Website"><circle cx="13" cy="13" r="12" fill="var(--brand-blue)"/><circle cx="13" cy="13" r="6.5" fill="none" stroke="#fff" stroke-width="1.4"/><ellipse cx="13" cy="13" rx="2.8" ry="6.5" fill="none" stroke="#fff" stroke-width="1.2"/><path d="M6.5 13h13" stroke="#fff" stroke-width="1.2"/></svg>
    </div>
    <p class="contact-line">708.214.8573</p>
    <p class="contact-line">derek@granitesurfaceworks.example</p>
    <p class="contact-line">www.<span class="accent">granitesurfaceworks.example</span></p>
  </div>

  <div class="address-band">
    <svg viewBox="0 0 22 28" aria-label="Location"><path d="M11 1C5.5 1 1.5 5 1.5 10.2 1.5 17 11 27 11 27s9.5-10 9.5-16.8C20.5 5 16.5 1 11 1z" fill="var(--brand-green)"/><circle cx="11" cy="10" r="3.6" fill="#fff"/></svg>
    <p class="address-line">4817 Willowmere Road PMB</p>
    <p class="address-line">5046 Nashville, TN 37209</p>
  </div>
</section>

<section class="card card-back" aria-label="Business card back">
  <div class="back-brand">
    <span class="brand-square"></span>
    <span class="brand-name">Granite Surface Works</span>
  </div>
  <p class="back-web">www.granitesurfaceworks.example</p>
</section>

</body>
</html>
```